Morvetta Designs - Online Shoe Shop

Morvetta is an online shoes and bags shop. We sell Imported Genuine Leather shoes and bags our market is LSM 8-10. We mainly sell women shoes and bags and we will also be introducing men’s shoes and belts.
I would like a website design and development that is responsive, clean, elegant and easy to use. Where customers can make a purchase online.
Have CATEGORIES in SHOE STYLE (i.e. Heels, Sandals, Pumps, Mules, Boots, Sneaker, Flats, etc) and PRICE RANGE should be in South African Rands currency, COLOUR, SIZE.
For shoe images we should be able to add videos as well.
Header and Footer Menu should have the basic menu list. Header Menu (New Arrivals, Preorder, Women’s Collection, Men’s Collection, Summer 2020 Collection, Winter 2020 Collection, Bags, Accessories, Sale, etc
Auto display when the item is SOLD OUT. Add an option for a user to get notification on when the item is back in stock.
Icons to show when shoes are on sale and Show was and now price.
Users to be able to review and rate the items.
Discount codes for new email subscribers.
Consumers should be able to pay using different options, Credit card, QuidLane, EFT, etc
Add an option for discount coupons at checkout.
After placing and order they should receive an email with order receipt.
Site should have a shipping and tracking option. International shipping such as KRT and BOLTAIR. For local shipping in South Africa please add Quickpath Couriers and Zenobi Couriers.
Backend: Backend should be easy to add more categories, items and changing header banners, adding sale alerts. To get notification when the stock is low and sold out. Get notification when an order is placed online so to prepare packing for shipping.
Can we make sure that the SEO is in place and bare in mind all searchy rules to avoid being penalized.
Target Market(s)
Women from age 25-65
LSM 8-10
Entire South Africa and neighboring countries
Industry/Entity Type
Shoe Store
Coding
Coded - Design and coding required
Number of Pages Required
5+ page
Requirements
Must have
- Responsive
Clean
Modern
Shopping cart
Shipping options integration
Newsletter subscription
Social media icons
Nice to have
- The business colors are Gold and White or Gold and Black

```html
<!DOCTYPE html>
<html lang="en">
<head>
<meta charset="utf-8">
<title>Morvetta – Women Red Heels</title>
<link rel="stylesheet" href="https://fonts.googleapis.com/css2?family=Raleway:wght@300;400;500;600;700;800&display=swap">
<style>
:root{
  --gold:#e9bc12;
  --gold-dark:#c89c06;
  --orange:#f47b20;
  --black:#1a1a1a;
  --nav:#2c2c2c;
  --footer:#1d1f22;
  --text:#222;
  --muted:#666;
  --line:#dcdcdc;
  --blue:#2f6fd6;
  --price:#e3a400;
}
*{box-sizing:border-box;margin:0;padding:0}
html,body{width:1200px;height:2449px;overflow:hidden}
body{font-family:"Raleway",sans-serif;color:var(--text);background:#fff;position:relative}
.abs{position:absolute}
.btn-gold{background:linear-gradient(#f0c816,var(--gold-dark));color:#fff;font-weight:600;text-align:center;text-transform:uppercase}

/* top bar */
.topbar{position:absolute;left:0;top:0;width:1200px;height:53px;background:var(--black)}
.social-dots{position:absolute;left:93px;top:14px;display:flex;gap:3px}
.social-dots span{width:23px;height:23px;border-radius:50%;background:#fff;display:block}
.deals{position:absolute;left:481px;top:11px;width:116px;height:30px;font-size:11px;line-height:30px}
.wholesale{position:absolute;left:602px;top:11px;width:116px;height:30px;background:#fff;font-size:11px;line-height:30px;text-align:center;color:#222}
.wholesale b{color:var(--gold);font-weight:500}
.top-icons{position:absolute;left:1020px;top:12px;display:flex;gap:10px;align-items:center}
.search-dot{width:28px;height:28px;border-radius:50%;background:#333;display:flex;align-items:center;justify-content:center}

/* nav */
.mainnav{position:absolute;left:0;top:53px;width:1200px;height:50px;background:var(--nav)}
.mainnav ul{list-style:none;display:flex;position:absolute;left:93px;top:0;height:50px;align-items:center;gap:31px;font-size:12px;color:#fff}
.lang{position:absolute;left:1025px;top:0;width:81px;height:50px;background:#1e1e1e;color:#fff;font-size:11px;display:flex;align-items:center;justify-content:center;gap:16px}
.lang b{color:var(--gold);font-weight:500}

/* header */
.header{position:absolute;left:0;top:103px;width:1200px;height:91px;border-bottom:1px solid #e6e6e6}
.logo{position:absolute;left:93px;top:6px;width:90px;text-align:center}
.logo .mark{width:46px;height:46px;background:#111;margin:0 auto 4px}
.logo .name{font-size:22px;font-weight:800;color:#111;letter-spacing:-.5px}
.welcome{position:absolute;left:787px;top:19px;font-size:11px;color:#222}
.login{position:absolute;left:855px;top:38px;width:79px;height:30px;font-size:11px;line-height:30px;text-transform:none;font-weight:500}
.cart{position:absolute;left:943px;top:22px;width:164px;height:46px;border:1px solid var(--line);display:flex}
.cart .ico{width:49px;border-right:1px solid var(--line);display:flex;align-items:center;justify-content:center}
.cart .txt{padding:9px 10px;font-size:10px;color:#555;line-height:13px}
.cart .txt small{color:#999;font-size:9px}

/* product */
.crumbs{position:absolute;left:93px;top:207px;font-size:9px;color:#888;text-transform:uppercase}
.crumbs b{color:#222;font-weight:500}
.main-photo{position:absolute;left:93px;top:246px;width:395px;height:354px;border:1px solid var(--line);background:#fff}
.main-photo .ph{position:absolute;left:36px;top:38px;width:320px;height:260px;background:radial-gradient(ellipse at 50% 55%,#f0302a 0%,#d91c1c 45%,#fff 72%)}
.fav{position:absolute;left:348px;top:16px}
.thumbs{position:absolute;left:93px;top:600px;display:flex;gap:4px}
.thumbs div{width:108px;height:81px;background:#f2f2f2;border:1px solid var(--line)}
.thumbs .t1{background:radial-gradient(ellipse,#e22 0%,#f5b5b5 35%,#fff 60%)}
.thumbs .t2{background:radial-gradient(ellipse,#d11 0%,#eaa 35%,#eee 60%)}
.thumbs .t3{background:radial-gradient(ellipse,#1f45d8 0%,#a9b9ef 35%,#eee 60%)}
.add-cart{position:absolute;left:93px;top:724px;width:196px;height:38px;font-size:13px;line-height:38px;font-weight:500}
.buy-now{position:absolute;left:293px;top:724px;width:195px;height:38px;background:var(--orange);color:#fff;font-size:13px;line-height:38px;text-align:center;font-weight:500}

.info{position:absolute;left:525px;top:244px;width:582px}
.info .brand{font-size:10px;color:#555}
.info h1{font-size:21px;font-weight:700;margin-top:4px;letter-spacing:.2px}
.info .price{font-size:16px;color:var(--price);font-weight:600;margin-top:4px}
.info .price small{font-size:9px;color:#e02020;font-weight:500;margin-left:12px}
.rating{display:flex;align-items:center;gap:6px;margin-top:4px;font-size:11px;color:#555}
.rating span{background:#1f8fe0;color:#fff;font-size:10px;padding:3px 8px;font-weight:600}
.offers h3{font-size:14px;font-weight:500;margin-top:18px}
.offers p{font-size:11px;color:#444;margin-top:6px}
.deliver{margin-top:22px;font-size:12px;font-weight:600}
.pin{width:196px;border-bottom:2px solid var(--blue);font-size:11px;color:#333;padding:8px 0 4px;display:flex;justify-content:space-between;padding-right:6px}
.usual{margin-top:26px;font-size:13px}
.usual-sub{font-size:11px;color:#555;margin-top:6px}
.view{margin-top:12px;font-size:12px;font-weight:600;text-decoration:underline;color:#333}
.opt-label{font-size:12px;font-weight:600}
.swatches{display:flex;gap:7px;margin-top:8px}
.swatches span{width:32px;height:32px;border-radius:50%}
.sizes{display:flex;gap:11px;margin-top:8px}
.sizes span{width:27px;height:27px;border:1px solid #999;font-size:13px;line-height:25px;text-align:center}
.pd{position:absolute;left:524px;top:744px;width:583px;border-bottom:1px solid var(--line);padding-bottom:10px;font-size:18px;font-weight:600}

/* product cards */
.section-title{position:absolute;left:92px;font-size:32px;font-weight:600;color:#333}
.row{position:absolute;left:93px;display:flex;gap:14px}
.card{width:244px;height:284px;border:1px solid var(--line);position:relative;background:#fff}
.card .img{position:absolute;left:30px;top:12px;width:184px;height:150px}
.card h4{position:absolute;left:14px;top:166px;font-size:17px;font-weight:400;color:#333}
.card .p{position:absolute;left:14px;top:191px;font-size:12px;color:var(--price);font-weight:600}
.card .stars{position:absolute;left:14px;top:212px;font-size:10px;color:var(--gold);letter-spacing:1px}
.card .cbtn{position:absolute;left:15px;top:234px;width:116px;height:30px;line-height:30px;font-size:10px}
.card .det{position:absolute;left:147px;top:242px;font-size:11px;color:#333}
.arrow{position:absolute;width:30px;height:30px;border-radius:50%;border:1px solid #bbb;background:#fff;display:flex;align-items:center;justify-content:center}
.tabs{position:absolute;left:94px;top:1319px;display:flex;gap:43px;font-size:13px;color:#444}
.tabs .on{color:#222;font-weight:600;border-bottom:2px solid var(--blue);padding-bottom:4px}

/* stories */
.hr{position:absolute;left:93px;top:1718px;width:1014px;height:1px;background:var(--line)}
.stories{position:absolute;left:93px;top:1762px;width:1014px}
.stories h2{font-size:24px;font-weight:400;color:#333}
.stories h2 b{font-weight:600}
.stories p{margin-top:14px;font-size:13px;line-height:21px;color:#666;text-transform:uppercase}

/* footer */
.footer{position:absolute;left:0;top:1911px;width:1200px;height:538px;background:var(--footer);color:#ccc}
.fcol{position:absolute;top:46px}
.fcol h5{font-size:18px;font-weight:600;color:#fff;margin-bottom:14px}
.fcol li{list-style:none;font-size:12px;color:#bbb;line-height:27px}
.news input{display:block;width:222px;height:29px;margin-bottom:5px;border:0;padding:0 9px;font-family:inherit;font-size:10px}
.news .sub{width:222px;height:29px;font-size:11px;line-height:29px}
.soc li{display:flex;align-items:center;gap:8px;line-height:30px}
.soc li i{width:22px;height:22px;border-radius:50%;background:#fff;display:block}
.fline{position:absolute;left:93px;width:1014px;height:1px;background:#3a3c40}
.feat{position:absolute;top:286px;display:flex;gap:22px;align-items:center}
.feat .circ{width:58px;height:58px;border-radius:50%;background:var(--gold);display:flex;align-items:center;justify-content:center}
.feat h6{font-size:14px;color:var(--gold);font-weight:700}
.feat p{font-size:11px;color:#aaa;line-height:13px;margin-top:2px}
.pay{position:absolute;left:0;top:391px;width:1200px;text-align:center;color:#fff}
.pay .s{font-size:7px;font-weight:600}
.pay .q{font-size:17px;font-weight:700;margin-top:1px}
.pay .cards{display:flex;justify-content:center;gap:3px;margin-top:10px}
.pay .cards span{width:26px;height:16px;border-radius:2px;display:block}
.copy{position:absolute;left:0;top:476px;width:1200px;text-align:center;font-size:12px;color:#bbb}
.copy b{color:var(--gold);font-weight:500}
</style>
</head>
<body>

<header>
  <div class="topbar">
    <div class="social-dots"><span></span><span></span><span></span><span></span><span></span></div>
    <div class="deals btn-gold">Latest Deals</div>
    <div class="wholesale">WHOLESALE <b>LOGIN</b></div>
    <div class="top-icons">
      <div class="search-dot"><svg width="12" height="12" viewBox="0 0 12 12"><circle cx="5" cy="5" r="3.6" fill="none" stroke="#e9bc12" stroke-width="1.8"/><line x1="7.6" y1="7.6" x2="11" y2="11" stroke="#e9bc12" stroke-width="2"/></svg></div>
      <svg width="18" height="16" viewBox="0 0 18 16"><circle cx="9" cy="5" r="4" fill="#fff"/><path d="M1 16c0-5 16-5 16 0z" fill="#fff"/></svg>
      <svg width="18" height="16" viewBox="0 0 18 16"><path d="M9 15L2 8a4 4 0 0 1 7-5 4 4 0 0 1 7 5z" fill="#fff"/></svg>
    </div>
  </div>
  <nav class="mainnav">
    <ul>
      <li>New Arrivals</li><li>Preorder</li><li>Women's Collection</li><li>Men's Collection</li><li>Summer 2020 Collection</li><li>Winter 2020 Collection</li><li>Bags</li><li>Accessories</li><li>Sale</li>
    </ul>
    <div class="lang"><span>En ⌄</span><b>$ ⌄</b></div>
  </nav>
  <div class="header">
    <div class="logo"><div class="mark"></div><div class="name">Morvetta</div></div>
    <div class="welcome">Welcome To our online store!</div>
    <div class="login btn-gold">⊕ Log In</div>
    <div class="cart">
      <div class="ico"><svg width="20" height="18" viewBox="0 0 20 18"><path d="M1 6h18l-3 11H4z" fill="#111"/><path d="M6 6l4-5 4 5" fill="none" stroke="#111" stroke-width="1.6"/></svg></div>
      <div class="txt">My Cart:<br><small>0 item(s)-$0.00</small></div>
    </div>
  </div>
</header>

<main>
  <div class="crumbs">Home &gt; Women's Shoes &gt; <b>Womens Heels New Cut</b></div>

  <div class="main-photo">
    <div class="ph" role="img" aria-label="Pair of red suede high heel pumps"></div>
    <svg class="fav" width="24" height="20" viewBox="0 0 24 20"><path d="M12 19L3 10a5 5 0 0 1 9-7 5 5 0 0 1 9 7z" fill="#d6d6d6"/></svg>
  </div>
  <div class="thumbs">
    <div class="t1" role="img" aria-label="Red heel side view"></div>
    <div class="t2" role="img" aria-label="Red heel angled view"></div>
    <div class="t3" role="img" aria-label="Blue heel colour option"></div>
  </div>
  <div class="add-cart btn-gold">Add To Cart</div>
  <div class="buy-now">BUY NOW</div>

  <section class="info">
    <div class="brand">LOREM</div>
    <h1>WOMEN RED HEELS LOREM</h1>
    <div class="price">R.583.95<small>Hurry, Only 3 left!</small></div>
    <div class="rating"><span>4.1 ★</span>110 ratings and 9 reviews</div>
    <div class="offers">
      <h3>Available offers</h3>
      <p>Bank Offer5% Unlimited Cashback on Morvetta Axton Bank Credit CardT&amp;C</p>
      <p>Bank OfferExtra 5% off* with Axton Bank Buzz Credit CardT&amp;C</p>
    </div>
    <div class="deliver">Deliver to</div>
    <div class="pin"><span>Enter delivery pincode</span><span>Check</span></div>
    <div class="usual">Usually delivered In3-4 days?</div>
    <div class="usual-sub">Enter pincode for exact delivery dates/charges</div>
    <div class="view">VIEW DETAILS</div>
    <div class="opt-label" style="margin-top:40px">Color</div>
    <div class="swatches"><span style="background:#e8192c"></span><span style="background:#2350e0"></span></div>
    <div class="opt-label" style="margin-top:16px">Size</div>
    <div class="sizes"><span>4</span><span>5</span><span>6</span><span>7</span></div>
  </section>
  <div class="pd">Product Details <span style="font-size:13px;margin-left:14px">›</span></div>

  <h2 class="section-title" style="top:866px">Similar Products</h2>
  <div class="arrow" style="left:32px;top:1059px">‹</div>
  <div class="arrow" style="left:1138px;top:1059px">›</div>
  <div class="row" style="top:931px">
    <div class="card"><div class="img" role="img" aria-label="Brown leather pumps" style="background:radial-gradient(ellipse,#4a3a30 0%,#8a7a70 35%,#fff 68%)"></div><h4>Eiusmod Tempor</h4><div class="p">R 583.95</div><div class="stars">★★★★★</div><div class="cbtn btn-gold">Add To Cart</div><div class="det">DETAILS</div></div>
    <div class="card"><div class="img" role="img" aria-label="Blue suede heel" style="background:radial-gradient(ellipse,#1f3fb0 0%,#8fa0d8 35%,#fff 68%)"></div><h4>Eiusmod Tempor</h4><div class="p">R 583.95</div><div class="stars">★★★★★</div><div class="cbtn btn-gold">Add To Cart</div><div class="det">DETAILS</div></div>
    <div class="card"><div class="img" role="img" aria-label="Red patent stiletto heels" style="background:radial-gradient(ellipse,#e01010 0%,#f08a8a 38%,#fff 68%)"></div><h4>Eiusmod Tempor</h4><div class="p">R 583.95</div><div class="stars">★★★★★</div><div class="cbtn btn-gold">Add To Cart</div><div class="det">DETAILS</div></div>
    <div class="card"><div class="img" role="img" aria-label="Yellow block heels with patterned heel" style="background:radial-gradient(ellipse,#e0a010 0%,#f0d080 38%,#fff 68%)"></div><h4>Eiusmod Tempor</h4><div class="p">R 583.95</div><div class="stars">★★★★★</div><div class="cbtn btn-gold">Add To Cart</div><div class="det">DETAILS</div></div>
  </div>

  <h2 class="section-title" style="top:1267px">Bought Together</h2>
  <div class="tabs"><span class="on">All Categories</span><span>Slippers &amp; Flip Flops</span><span>Men's Collection</span><span>Handbags</span></div>
  <div class="arrow" style="left:32px;top:1512px">‹</div>
  <div class="arrow" style="left:1138px;top:1512px">›</div>
  <div class="row" style="top:1384px">
    <div class="card"><div class="img" role="img" aria-label="Gold evening handbag" style="background:radial-gradient(ellipse,#c8a860 0%,#e6d4a8 38%,#fff 68%)"></div><h4>Eiusmod Tempor</h4><div class="p">R 583.95</div><div class="stars">★★★★★</div><div class="cbtn btn-gold">Add To Cart</div><div class="det">DETAILS</div></div>
    <div class="card"><div class="img" role="img" aria-label="Black ballet flats" style="background:radial-gradient(ellipse,#222 0%,#999 35%,#fff 68%)"></div><h4>Eiusmod Tempor</h4><div class="p">R 583.95</div><div class="stars">★★★★★</div><div class="cbtn btn-gold">Add To Cart</div><div class="det">DETAILS</div></div>
    <div class="card"><div class="img" role="img" aria-label="Brown leather belt" style="background:radial-gradient(ellipse,#8a4a20 0%,#c8a080 38%,#fff 68%)"></div><h4>Eiusmod Tempor</h4><div class="p">R 583.95</div><div class="stars">★★★★★</div><div class="cbtn btn-gold">Add To Cart</div><div class="det">DETAILS</div></div>
    <div class="card"><div class="img" role="img" aria-label="Yellow leather handbag" style="background:radial-gradient(ellipse,#f0d010 0%,#f6e680 40%,#fff 68%)"></div><h4>Eiusmod Tempor</h4><div class="p">R 583.95</div><div class="stars">★★★★★</div><div class="cbtn btn-gold">Add To Cart</div><div class="det">DETAILS</div></div>
  </div>

  <div class="hr"></div>
  <section class="stories">
    <h2>Top Stories: <b>Brand Directory</b></h2>
    <p>Sed ut perspiciatis unde omnis iste natus error sit voluptatem accusantium doloremque laudantium, totam rem aperiam, eaque ipsa quae ab illo inventore veritatis et quasi architecto beatae vitae dicta sunt explicabo. Nemo enim ipsam voluptatem quia voluptas sit aspernatur aut odit aut fugit sed quia consequuntur magni dolores eos qui ratione</p>
  </section>
</main>

<footer class="footer">
  <div class="fcol" style="left:94px"><h5>ABOUT</h5><ul><li>Contact Us</li><li>About Us</li><li>Careers</li><li>Morvetta Stories</li><li>Press</li></ul></div>
  <div class="fcol" style="left:286px"><h5>HELP</h5><ul><li>Payments</li><li>Shipping</li><li>Cancellation &amp; Returns</li><li>FAQ</li><li>Report Infringement</li></ul></div>
  <div class="fcol" style="left:521px"><h5>POLICY</h5><ul><li>Return Policy</li><li>Terms Of Use</li><li>Security</li><li>Privacy</li><li>Sitemap</li></ul></div>
  <div class="fcol news" style="left:714px"><h5>NEWSLETTER</h5><input placeholder="Enter Name:"><input placeholder="Enter Email:"><div class="sub btn-gold">Subscribe</div></div>
  <div class="fcol soc" style="left:1021px"><h5>SOCIAL</h5><ul><li><i></i>Circlebook</li><li><i></i>Chirpline</li><li><i></i>Pictora</li><li><i></i>Vidstream</li><li><i></i>RSS</li></ul></div>

  <div class="fline" style="top:259px"></div>
  <div class="feat" style="left:94px"><div class="circ"><svg width="32" height="22" viewBox="0 0 32 22"><rect x="1" y="3" width="19" height="13" fill="#111"/><path d="M20 7h6l4 5v4H20z" fill="#111"/><circle cx="7" cy="18" r="3" fill="#111"/><circle cx="25" cy="18" r="3" fill="#111"/></svg></div><div><h6>FREE SHIPPING</h6><p>Sed ut perspiciatis unde omnis iste<br>natus error sit voluptatem</p></div></div>
  <div class="feat" style="left:469px"><div class="circ"><svg width="30" height="22" viewBox="0 0 30 22"><rect x="2" y="3" width="26" height="16" rx="2" fill="none" stroke="#111" stroke-width="2"/><rect x="2" y="7" width="26" height="3" fill="#111"/></svg></div><div><h6>SECURED PAYMENT</h6><p>Sed ut perspiciatis unde omnis iste<br>natus error sit voluptatem</p></div></div>
  <div class="feat" style="left:838px"><div class="circ"><svg width="30" height="28" viewBox="0 0 30 28"><circle cx="19" cy="10" r="7" fill="none" stroke="#111" stroke-width="2"/><path d="M2 22h8l6 3 10-5v-2l-9 2H10l-8-2z" fill="#111"/></svg></div><div><h6>MONEY BACK GUARANTEE</h6><p>Sed ut perspiciatis unde omnis iste<br>natus error sit voluptatem</p></div></div>
  <div class="fline" style="top:367px"></div>

  <div class="pay">
    <div class="s">Secure Payments by</div>
    <div class="q">QuidLane</div>
    <div class="cards"><span style="background:#e8452a"></span><span style="background:#1a3a8c"></span><span style="background:#2a8ad0"></span><span style="background:#eee"></span></div>
  </div>
  <div class="copy">Copyright © 2020 <b>Morvetta</b>. All rights reserved.</div>
</footer>

</body>
</html>
```